Rallypoint Forge is a web based program in the sports industry. We are looking for a modern, cutting edge business card design. We are looking for a dark base and need to use three logo's on the card. Rallypoint Forge, Vantora Sports Supplements, and Elmbrook Golf Academy.
Updates

This project is guaranteed. Not sure how to do that....

Industry/Entity Type

Business

Requirements
Must have
• 3 logo's... Rallypoint Forge... Elmbrook Golf Academy... VanTora Sports Supplements

```html
<!DOCTYPE html>
<html lang="en">
<head>
<meta charset="utf-8">
<title>Rallypoint Forge Business Card</title>
<link rel="stylesheet" href="https://fonts.googleapis.com/css2?family=Montserrat:wght@400;500;600;700;800&display=swap">
<style>
  :root {
    --backdrop: #e9e6e2;
    --card-white: #ffffff;
    --ink: #1d1d1f;
    --brand-red: #c41f33;
    --brand-red-deep: #a8182a;
    --badge-red: #e8323f;
    --contact-white: #ffffff;
  }
  * { margin: 0; padding: 0; box-sizing: border-box; }
  html, body {
    width: 1200px; height: 900px; overflow: hidden;
    background: var(--backdrop);
    font-family: "Montserrat", Arial, sans-serif;
  }
  .sheet {
    width: 1200px; height: 900px;
    display: flex; flex-direction: column;
    align-items: center; justify-content: center; gap: 40px;
  }
  .card {
    width: 700px; height: 400px;
    background: var(--card-white);
    box-shadow: 0 6px 18px rgba(0,0,0,.18);
    position: relative; overflow: hidden;
  }
  /* logo group shared by both sides */
  .logo-group { display: flex; flex-direction: column; align-items: flex-start; }
  .wordmark {
    display: flex; align-items: center; gap: 12px;
    font-weight: 800; color: var(--ink); line-height: .95;
  }
  .wordmark-dot { border-radius: 50%; background: var(--ink); flex: none; }
  .partner-row { display: flex; align-items: center; gap: 18px; margin-top: 16px; }
  .golf-academy {
    display: flex; align-items: center; gap: 8px;
    font-weight: 700; color: var(--ink); line-height: 1.05;
  }
  .golf-academy-ring {
    border: 3px solid var(--brand-red); border-radius: 50%; flex: none;
  }
  .supplement-badge {
    background: var(--badge-red); color: var(--contact-white);
    font-weight: 700; text-align: center;
    display: flex; flex-direction: column; justify-content: center;
    letter-spacing: .08em;
  }
  .supplement-badge small { font-weight: 700; letter-spacing: .18em; }

  /* back side: logos only */
  .card-back { display: flex; align-items: center; justify-content: center; }
  .card-back .wordmark { font-size: 46px; }
  .card-back .wordmark-dot { width: 26px; height: 26px; }
  .card-back .golf-academy { font-size: 15px; }
  .card-back .golf-academy-ring { width: 30px; height: 30px; }
  .card-back .supplement-badge { width: 160px; height: 62px; font-size: 19px; }
  .card-back .supplement-badge small { font-size: 7px; margin-top: 3px; }

  /* front side: logos + contact panel */
  .card-front { display: flex; }
  .front-logos {
    width: 44%; display: flex; align-items: center; justify-content: center;
    background: linear-gradient(180deg, #ffffff, #f4f4f4);
  }
  .card-front .wordmark { font-size: 36px; }
  .card-front .wordmark-dot { width: 20px; height: 20px; }
  .card-front .partner-row { gap: 12px; margin-top: 14px; }
  .card-front .golf-academy { font-size: 12px; }
  .card-front .golf-academy-ring { width: 24px; height: 24px; border-width: 2.5px; }
  .card-front .supplement-badge { width: 128px; height: 52px; font-size: 15px; }
  .card-front .supplement-badge small { font-size: 6px; margin-top: 3px; }

  .contact-panel {
    width: 56%;
    background: linear-gradient(160deg, var(--brand-red), var(--brand-red-deep));
    color: var(--contact-white);
    padding: 44px 40px 0 42px;
  }
  .holder-name { font-size: 26px; font-weight: 600; letter-spacing: .01em; }
  .address { margin-top: 74px; font-size: 14px; line-height: 1.35; }
  .contact-list { list-style: none; margin-top: 26px; font-size: 14px; }
  .contact-list li { display: flex; align-items: center; gap: 14px; line-height: 1.45; }
  .contact-icon { width: 14px; height: 14px; flex: none; }
</style>
</head>
<body>
<main class="sheet">

  <section class="card card-back" aria-label="Card back">
    <div class="logo-group">
      <div class="wordmark"><span class="wordmark-dot"></span><span>Rallypoint<br>Forge</span></div>
      <div class="partner-row">
        <div class="golf-academy"><span class="golf-academy-ring"></span><span>Elmbrook Golf<br>Academy</span></div>
        <div class="supplement-badge">VANTORA<small>SPORTS SUPPLEMENTS</small></div>
      </div>
    </div>
  </section>

  <section class="card card-front" aria-label="Card front">
    <div class="front-logos">
      <div class="logo-group">
        <div class="wordmark"><span class="wordmark-dot"></span><span>Rallypoint<br>Forge</span></div>
        <div class="partner-row">
          <div class="golf-academy"><span class="golf-academy-ring"></span><span>Elmbrook Golf<br>Academy</span></div>
          <div class="supplement-badge">VANTORA<small>SPORTS SUPPLEMENTS</small></div>
        </div>
      </div>
    </div>
    <div class="contact-panel">
      <h1 class="holder-name">Dana Whitcombe</h1>
      <p class="address">4820 Larkspur Fairway Dr<br>Clermont Ridge, FL 34790</p>
      <ul class="contact-list">
        <li>
          <svg class="contact-icon" viewBox="0 0 16 16" aria-hidden="true"><path fill="#fff" d="M2 5c0-2 2-3 6-3s6 1 6 3v1h-3V5H5v1H2zM4 7h8l2 6H2z"/><circle cx="8" cy="10" r="1.6" fill="#c41f33"/></svg>
          <span>407.555.0148</span>
        </li>
        <li>
          <svg class="contact-icon" viewBox="0 0 16 16" aria-hidden="true"><rect x="1.5" y="3.5" width="13" height="9" fill="none" stroke="#fff" stroke-width="1.4"/><path d="M1.5 3.5l6.5 5 6.5-5" fill="none" stroke="#fff" stroke-width="1.4"/></svg>
          <span>dana@rallypointforge.com</span>
        </li>
        <li>
          <svg class="contact-icon" viewBox="0 0 16 16" aria-hidden="true"><circle cx="8" cy="8" r="6.3" fill="none" stroke="#fff" stroke-width="1.4"/><ellipse cx="8" cy="8" rx="2.6" ry="6.3" fill="none" stroke="#fff" stroke-width="1.1"/><path d="M1.7 8h12.6" stroke="#fff" stroke-width="1.1"/></svg>
          <span>www.rallypointforge.com</span>
        </li>
        <li>
          <svg class="contact-icon" viewBox="0 0 16 16" aria-hidden="true"><rect x="1.5" y="1.5" width="13" height="13" rx="2" fill="#fff"/></svg>
          <span>@RallypointForge</span>
        </li>
      </ul>
    </div>
  </section>

</main>
</body>
</html>
```